Personal training poster

Hi, I need a poster designed for my personal training business to help attracted some new clients over these quiet months. I want the poster to be eye catching and something that I can put up in the gym when I need to attract some new business, so it can no be seasional (i.e) Winter, Summer reference.

My logo has to be includes (Brookvale Strength & Diet)

Target Market(s)

New clients within a gym envitoment

Industry/Entity Type

Fitness

Font styles to use
Serif

Colors

Designer to choose colors to be used in the design.

Requirements
Must have
• My Logo
• Personal training introductory offer 4 X 45min sessions $180
• STOP WISHING. START DOING.
• Want to loose weight and or build muscle?
• Want to feel healthier and fitter
• Want to learn proper/safe techique?
• Please contact Owen @ brookvalestrength@mailquay.net or phone 0427581946
• *conditions apply at the bottom
Nice to have
• My facebook and instagram
• brookvale_strength_diet (instagram)
• Brookvale Strength & Diet (facebook)
• Eat Clean, Train Dirty
Should not have
• Imiges of Femaile trainers as I am a Male

```html
<!DOCTYPE html>
<html lang="en">
<head>
<meta charset="utf-8">
<title>Brookvale Strength &amp; Diet – Stop Wishing Start Doing</title>
<link rel="stylesheet" href="https://fonts.googleapis.com/css2?family=Oswald:wght@300;400;600;700&display=swap">
<style>
  :root {
    --ink: #0d0d0d;
    --charcoal: #1a1a1a;
    --steel: #6f6f6f;
    --band-grey: #8a8a8a;
    --red: #c8102e;
    --red-deep: #9e0c22;
    --white: #ffffff;
    --muted: #c4c4c4;
  }
  * { margin: 0; padding: 0; box-sizing: border-box; }
  html, body { width: 849px; height: 1200px; overflow: hidden; background: var(--ink); }
  .poster {
    position: relative; width: 849px; height: 1200px; overflow: hidden;
    background: var(--ink);
    font-family: "Oswald", "Arial Narrow", sans-serif;
    color: var(--white);
  }
  .photo-top {
    position: absolute; left: 0; top: 0; width: 849px; height: 600px;
    background:
      radial-gradient(ellipse 260px 320px at 660px 200px, #9a9a9a 0%, #4a4a4a 45%, transparent 80%),
      linear-gradient(180deg, #262626 0%, #161616 100%);
  }
  .photo-bottom {
    position: absolute; left: 0; top: 560px; width: 849px; height: 560px;
    background:
      radial-gradient(ellipse 280px 200px at 220px 230px, #7a7a7a 0%, #3a3a3a 50%, transparent 85%),
      linear-gradient(180deg, #1e1e1e 0%, #2a2a2a 60%, #111 100%);
  }
  .bands { position: absolute; left: 0; top: 0; }
  .slogan { position: absolute; text-transform: uppercase; line-height: 1; }
  .slogan .strong { display: block; font-weight: 700; font-size: 66px; letter-spacing: 1px; }
  .slogan .light { display: block; font-weight: 300; font-size: 62px; letter-spacing: 1px; margin-top: 4px; }
  .slogan--stop { right: 330px; top: 430px; text-align: right; }
  .slogan--start { left: 550px; top: 438px; }

  .offer {
    position: absolute; left: 500px; top: 700px; width: 320px;
    text-align: right;
  }
  .offer-label { font-size: 17px; font-weight: 400; letter-spacing: 2px; text-transform: uppercase; color: var(--muted); }
  .offer-deal { font-size: 34px; font-weight: 700; line-height: 1.1; text-transform: uppercase; margin-top: 4px; }
  .offer-price { color: var(--red); }
  .benefits { list-style: none; margin-top: 14px; font-size: 17px; font-weight: 300; line-height: 1.45; }
  .motto { margin-top: 10px; font-size: 17px; font-weight: 600; letter-spacing: 2px; text-transform: uppercase; color: var(--red); }

  .brand {
    position: absolute; left: 0; right: 0; top: 920px;
    display: flex; flex-direction: column; align-items: center;
    color: var(--red); font-weight: 600; text-transform: uppercase;
  }
  .brand-dot { width: 16px; height: 16px; border-radius: 50%; background: var(--red); margin-bottom: 10px; }
  .brand-name { font-size: 64px; letter-spacing: 8px; line-height: 1; }
  .brand-sub { font-size: 24px; letter-spacing: 6px; margin-top: 6px; }
  .contact {
    position: absolute; left: 0; right: 0; top: 1082px;
    text-align: center; font-size: 17px; font-weight: 400; color: var(--muted);
  }
  .contact strong { color: var(--white); font-weight: 600; }

  .footer {
    position: absolute; left: 0; bottom: 0; width: 849px; height: 80px;
    background: var(--charcoal);
    display: flex; flex-direction: column; align-items: center; justify-content: center; gap: 6px;
  }
  .socials { display: flex; align-items: center; gap: 110px; font-size: 18px; color: var(--muted); }
  .social { display: flex; align-items: center; gap: 12px; }
  .social-mark { width: 22px; height: 22px; background: var(--steel); border-radius: 3px; }
  .conditions { font-size: 12px; font-weight: 300; color: var(--steel); letter-spacing: 1px; }
</style>
</head>
<body>
<main class="poster">
  <div class="photo-top" role="img" aria-label="Black and white gym photo of a muscular man curling a dumbbell"></div>
  <div class="photo-bottom" role="img" aria-label="Black and white gym photo of a dumbbell row on a bench in front of a weight rack"></div>

  <svg class="bands" width="849" height="1200" viewBox="0 0 849 1200" aria-hidden="true">
    <polygon points="0,470 540,390 540,560 0,640" fill="var(--red)"/>
    <polygon points="0,470 540,390 540,400 0,480" fill="var(--red-deep)" opacity="0.5"/>
    <polygon points="525,395 849,350 849,610 525,660" fill="var(--band-grey)" opacity="0.92"/>
  </svg>

  <h1 class="slogan slogan--stop"><span class="strong">Stop</span><span class="light">Wishing</span></h1>
  <h2 class="slogan slogan--start"><span class="strong">Start</span><span class="light">Doing</span></h2>

  <section class="offer">
    <p class="offer-label">Personal training introductory offer</p>
    <p class="offer-deal">4 × 45min sessions <span class="offer-price">$180*</span></p>
    <ul class="benefits">
      <li>Want to lose weight and/or build muscle?</li>
      <li>Want to feel healthier and fitter?</li>
      <li>Want to learn proper, safe technique?</li>
    </ul>
    <p class="motto">Eat Clean, Train Dirty</p>
  </section>

  <div class="brand">
    <span class="brand-dot"></span>
    <span class="brand-name">Brookvale</span>
    <span class="brand-sub">Strength &amp; Diet</span>
  </div>

  <p class="contact">Contact <strong>Owen</strong> @ brookvalestrength@mailquay.net or phone <strong>0427581946</strong></p>

  <footer class="footer">
    <div class="socials">
      <div class="social"><span class="social-mark"></span><span>Brookvale Strength &amp; Diet</span></div>
      <div class="social"><span class="social-mark"></span><span>brookvale_strength_diet</span></div>
    </div>
    <p class="conditions">*Conditions apply</p>
  </footer>
</main>
</body>
</html>
```